依頼概要
■依頼の目的/概要
当方、飲食店を4店舗経営しております
1.創作居酒屋
2.イタリアン+鮨
3.和食居酒屋
4.鮨+鉄板焼
以上4店舗です。
この度、新型コロナウイルスの影響で
お客様がご来店されなくなり
急遽、テイクアウトとデリバリーに力を
入れていこうと決めました。
そこで、魅力のあるメニューを作りたい
と考えております。
■要望のポイント
今回のメニューは先程あげました4店舗のメニューがそれぞれ入っております。
和と洋をイメージできるような、おしゃれな感じを望んでいます。お客様の層は幅広いですが、女性の方が多いです。
■その他注意点など
店内のイメージは
写真を送ることも可能ですが
菜ダイニング灯で検索していただけると
画像が出ると思います。
できればイメージの統一感があればいいなと思います。
メニューの内容や
写真はお送りいたします。
後ほど、写真の追加があります?
その他何かご不明点ただがあれば
お気軽にご質問ください
よろしくお願い致します
ロゴや料理写真を添付いたしました。
料理の写真は、店内メニュー用の写真なので
器とかが変わってしまいます。
ですので、このような料理です的なイメージみたいな感じでお願いできますでしょうか?
料理写真です。
宜しくお願いいたします。
ロゴです!
宜しくお願いいたします。
メニュー写真の追加です
全部の写真を使わなくても大丈夫です!
宜しくお願いいたします。
お弁当の写真です!
宜しくお願いいたします。
■ 選んだ理由

こちらの意向が伝わりやすく、イメージより良かったからです!!!

■ 提案者全員のお礼・コメント

毎月少しづつ内容やデザインを変えてやりたいと思っているので、またご縁があればうれしいなと思います!本当に素早いご対応ありがとうございます!

```html
<!DOCTYPE html>
<html lang="ja">
<head>
<meta charset="utf-8">
<title>テイクアウト＆デリバリー | 菜ダイニング灯</title>
<link rel="stylesheet" href="https://fonts.googleapis.com/css2?family=M+PLUS+Rounded+1c:wght@500;800;900&family=Noto+Sans+JP:wght@400;700;900&display=swap">
<style>
  :root {
    --red: #e2262b;
    --deep-red: #b3161b;
    --pink: #f7c9c4;
    --blush: #fbe3df;
    --slate: #5d7ea6;
    --white: #ffffff;
    --ink: #3a2a26;
    --food-dark: #2a1a14;
    --food-warm: #8a3d22;
    --food-light: #d9a46a;
  }
  * { margin: 0; padding: 0; box-sizing: border-box; }
  html, body { width: 846px; height: 1200px; overflow: hidden; background: var(--white); }
  .flyer {
    position: relative;
    width: 846px; height: 1200px;
    overflow: hidden;
    font-family: "Noto Sans JP", sans-serif;
    color: var(--ink);
  }
  .food-photo {
    position: absolute; inset: 0 0 260px 0;
    background:
      radial-gradient(ellipse at 30% 20%, var(--food-light) 0%, transparent 45%),
      radial-gradient(ellipse at 75% 45%, #c65a3a 0%, transparent 40%),
      radial-gradient(ellipse at 25% 70%, var(--food-warm) 0%, transparent 45%),
      linear-gradient(160deg, #4a2d1f 0%, var(--food-dark) 100%);
  }
  .photo-fade {
    position: absolute; left: 0; right: 0; top: 620px; height: 320px;
    background: linear-gradient(180deg, rgba(251,227,223,0) 0%, rgba(251,227,223,.85) 55%, var(--white) 100%);
  }
  .tagline {
    position: absolute; left: 150px; top: 40px;
    transform: rotate(-12deg);
    font-family: "M PLUS Rounded 1c", sans-serif; font-weight: 900;
    color: var(--white); text-align: center; line-height: 1.1;
  }
  .tagline .small { display: inline-block; font-size: 32px; background: var(--slate); padding: 2px 16px; border-radius: 22px; }
  .tagline .brand { display: inline-block; margin-top: 4px; font-size: 40px; background: var(--slate); padding: 2px 20px; border-radius: 26px; }
  .headline {
    position: absolute;
    writing-mode: vertical-rl;
    font-family: "M PLUS Rounded 1c", sans-serif; font-weight: 900;
    color: var(--red); line-height: 1;
    white-space: nowrap;
    text-shadow:
      4px 0 0 var(--white), -4px 0 0 var(--white), 0 4px 0 var(--white), 0 -4px 0 var(--white),
      3px 3px 0 var(--white), -3px 3px 0 var(--white), 3px -3px 0 var(--white), -3px -3px 0 var(--white),
      0 6px 14px rgba(0,0,0,.45);
    letter-spacing: -2px;
  }
  .headline--takeout { left: 540px; top: 50px; font-size: 82px; }
  .headline--delivery { left: 222px; top: 330px; font-size: 96px; }
  .ampersand {
    position: absolute; left: 395px; top: 455px;
    font-family: "M PLUS Rounded 1c", sans-serif; font-weight: 900;
    font-size: 80px; line-height: 1; color: var(--red);
    text-shadow: 3px 0 0 var(--white), -3px 0 0 var(--white), 0 3px 0 var(--white), 0 -3px 0 var(--white);
  }
  .invite {
    position: absolute; left: 510px; top: 640px; width: 320px;
    font-weight: 700; font-size: 21px; line-height: 1.6;
    color: var(--deep-red); text-align: center;
  }
  .home-badge {
    position: absolute; left: 22px; top: 735px;
    width: 150px; height: 150px; border-radius: 50%;
    background: var(--pink);
    display: flex; align-items: center; justify-content: center;
    font-family: "M PLUS Rounded 1c", sans-serif; font-weight: 900;
    font-size: 27px; line-height: 1.25; color: var(--red); text-align: center;
    transform: rotate(-8deg);
  }
  .stores {
    position: absolute; left: 30px; top: 905px; width: 470px;
    display: grid; grid-template-columns: 1fr 1fr; gap: 34px 20px;
  }
  .store-name {
    display: flex; align-items: center; gap: 10px;
    font-weight: 700; font-size: 26px; color: var(--ink); height: 90px;
  }
  .store-name .mark { width: 16px; height: 16px; border-radius: 50%; background: var(--red); flex: none; }
  .pickup { position: absolute; left: 520px; top: 890px; width: 310px; }
  .pickup-label {
    background: var(--red); color: var(--white);
    font-weight: 700; font-size: 18px; text-align: center; padding: 4px 0;
  }
  .pickup-name { margin-top: 12px; font-weight: 900; font-size: 34px; text-align: center; }
  .pickup-address { font-size: 11px; text-align: center; margin-top: 2px; }
  .pickup-tel {
    display: flex; align-items: baseline; justify-content: center; gap: 4px;
    margin-top: 8px; font-weight: 900; color: var(--ink); white-space: nowrap;
  }
  .pickup-tel svg { align-self: center; }
  .pickup-tel .label { font-size: 24px; }
  .pickup-tel .number { font-size: 38px; letter-spacing: -1px; }
  .pickup-hours { margin-top: 6px; font-size: 17px; font-weight: 700; text-align: center; white-space: nowrap; }
  .pickup-hours .time { font-size: 23px; }
  .pickup-notes { margin-top: 10px; font-size: 11px; line-height: 1.5; text-align: center; }
</style>
</head>
<body>
<main class="flyer">
  <div class="food-photo" role="img" aria-label="刺身、卵焼き、ステーキ、いくら丼などが詰まった仕出し弁当の料理写真"></div>
  <div class="photo-fade"></div>

  <div class="tagline">
    <span class="small">おうちで</span><br>
    <span class="brand">AKARIを♪</span>
  </div>

  <h1 class="headline headline--takeout">テイクアウト</h1>
  <div class="ampersand">&amp;</div>
  <h1 class="headline headline--delivery">デリバリー</h1>

  <p class="invite">ぜひお家でも<br>AKARIの料理を<br>お楽しみください。</p>

  <div class="home-badge">ご自宅まで<br>お届け<br>します♪</div>

  <section class="stores">
    <div class="store-name"><span class="mark"></span>菜ダイニング灯</div>
    <div class="store-name"><span class="mark"></span>居酒屋 灯衛門</div>
    <div class="store-name"><span class="mark"></span>Lume</div>
    <div class="store-name"><span class="mark"></span>鮨 楓</div>
  </section>

  <section class="pickup">
    <div class="pickup-label">テイクアウト受け取り場所</div>
    <div class="pickup-name">菜ダイニング灯</div>
    <div class="pickup-address">〒030-0000 青森市灯町1丁目2-3 灯ビル1F</div>
    <div class="pickup-tel">
      <svg width="26" height="26" viewBox="0 0 24 24" aria-hidden="true"><path fill="#3a2a26" d="M6.6 10.8a15.2 15.2 0 0 0 6.6 6.6l2.2-2.2a1 1 0 0 1 1-.25 11.4 11.4 0 0 0 3.6.57 1 1 0 0 1 1 1V20a1 1 0 0 1-1 1A17 17 0 0 1 3 4a1 1 0 0 1 1-1h3.5a1 1 0 0 1 1 1c0 1.25.2 2.45.57 3.57a1 1 0 0 1-.25 1z"/></svg>
      <span class="label">TEL</span><span class="number">017-555-0148</span>
    </div>
    <div class="pickup-hours">お引き取り時間 <span class="time">17:00〜22:00</span></div>
    <p class="pickup-notes">お支払いは現金・各種クレジット<br>QR決済がご利用頂けます。</p>
  </section>
</main>
</body>
</html>
```